Core values in our company OTK (Oversight and Transit Keepers)

Do good:
1. Being Direct and communicative for the benefit of all parties
2. Working for the Benefit of the company, client and team members
3. Wanting to improve to create a better impact
4. Having healthy rivalry
Be ahead of curve:
1. Having the confidence to break through barriers which arise
2. Desire to grow and learn towards establishment and agreed goal
3. Getting off the sidelines and get into the game
4. Keeping the end game in mind having due regard to processes and milestones
5. Self starter and works on own initiative
6. Diligent and impactful in your field of responsibility
Truth and Honesty
2. Have the confidence and ability to speak what you really want to communicate
3. Being truthful to yourself, clients and colleagues to find the innovations that lie within
4. Seeking the truth by opening things up for discussion
5. Being Optimistic
Background Information on our Company:OTK is a professional law firm in London Docklands. We caters for both private and corporate clients ranging from highly regarded and established law firms to boutique and niche immigration practices. We also specialises in expert legal advice and prides itself on providing services that go beyond the expectations of its clients.
What we need: We need a Poster about Truth and Honesty, this is to show one of our values as a company. It will need to be vibrant and straight to the point. Colours can be orange grey white and yellow. Attached is our company logo.
Reason: To remind colleagues that this is one of our main values and it is instilled in our company.
Things we would like:
1. To create a point of focus
2. Use shapes to create visual interest
3. Use creative illustrations
4. Take the viewer’s focus on a journey with clever perspective
Industry/Entity Type
Legal
Requirements
Must have
- a globe (Picture)
- Do good:
- 1. Being Direct and communicative for the benefit of all parties
- 2. Working for the Benefit of the company, client and team members
- 3. Wanting to improve to create a better impact
- 4. Having healthy rivalry
- Be ahead of curve:
- 1. Having the confidence to break through barriers which arise
- 2. Desire to grow and learn towards establishment and agreed goal
- 3. Getting off the sidelines and get into the game
- 4. Keeping the end game in mind having due regard to processes and milestones
- 5. Self starter and works on own initiative
- 6. Diligent and impactful in your field of responsibility
- Truth and Honesty
- 2. Have the confidence and ability to speak what you really want to communicate
- 3. Being truthful to yourself, clients and colleagues to find the innovations that lie within
- 4. Seeking the truth by opening things up for discussion
- 5. Being Optimistic

```html
<!DOCTYPE html>
<html lang="en">
<head>
<meta charset="utf-8">
<title>OTK Core Values</title>
<link href="https://fonts.googleapis.com/css2?family=Roboto+Condensed:wght@400;500&display=swap" rel="stylesheet">
<style>
  :root {
    --cream: #fff8dc;
    --cream-deep: #fde9a8;
    --orange: #f7931e;
    --yellow: #fcc31e;
    --charcoal: #3f3d39;
    --ink: #1c1b19;
    --brand-grey: #4a4844;
  }
  * { margin: 0; padding: 0; box-sizing: border-box; }
  html, body { width: 848px; height: 1200px; overflow: hidden; }
  body {
    position: relative;
    font-family: "Roboto Condensed", "Arial Narrow", sans-serif;
    color: var(--ink);
    background: var(--cream);
  }
  .values-panel {
    position: absolute; left: 0; top: 0; width: 486px; height: 1200px;
    background: radial-gradient(ellipse at 55% 12%, var(--cream-deep) 0%, #fff3c4 35%, var(--cream) 75%);
  }
  .brand {
    position: absolute; left: 0; width: 486px; top: 62px; text-align: center;
    color: var(--brand-grey); font-weight: 500;
  }
  .brand-name { font-size: 96px; line-height: 1; letter-spacing: 4px; }
  .brand-full { font-size: 20px; margin-top: 10px; letter-spacing: 0.5px; }

  .value-title {
    position: absolute; left: 51px;
    height: 47px; padding: 0 11px;
    border-radius: 10px;
    font-size: 39px; line-height: 47px; font-weight: 400;
    color: #fff;
  }
  .value-title::after {
    content: ""; position: absolute; left: 18px; bottom: -13px;
    border-left: 9px solid transparent; border-right: 9px solid transparent;
    border-top: 14px solid var(--tab);
  }
  .title-good { top: 238px; background: var(--orange); --tab: var(--orange); }
  .title-curve { top: 501px; background: var(--yellow); --tab: var(--yellow); }
  .title-truth { top: 851px; background: var(--charcoal); --tab: var(--charcoal); }

  .value-list {
    position: absolute; left: 37px; width: 440px; list-style: none;
    font-size: 19px; line-height: 24px;
  }
  .value-list::before {
    content: ""; position: absolute; left: 5px; top: 8px; bottom: 12px; width: 3px;
    background: var(--mark);
  }
  .value-list li { position: relative; padding-left: 25px; margin-bottom: 9px; }
  .value-list li::before {
    content: ""; position: absolute; left: 0; top: 5px; width: 13px; height: 13px;
    background: var(--mark);
  }
  .list-good { top: 302px; --mark: var(--orange); }
  .list-curve { top: 563px; --mark: var(--yellow); }
  .list-truth { top: 913px; --mark: var(--charcoal); }

  .photo { position: absolute; left: 486px; width: 362px; }
  .photo-sand { top: 0; height: 407px;
    background: linear-gradient(160deg, #b9b3bd 0%, #a59fab 45%, #8f8996 100%); }
  .photo-growth { top: 407px; height: 377px;
    background: radial-gradient(ellipse at 60% 45%, #eef1f4 0%, #d9dde2 55%, #b9bec6 100%); }
  .photo-stones { top: 784px; height: 416px;
    background: linear-gradient(170deg, #3f5a2e 0%, #55643e 30%, #8b8a80 62%, #a3a199 100%); }
</style>
</head>
<body>
  <section class="values-panel">
    <header class="brand">
      <div class="brand-name">OTK</div>
      <div class="brand-full">Oversight and Transit Keepers</div>
    </header>

    <h2 class="value-title title-good">DO GOOD:</h2>
    <ul class="value-list list-good">
      <li>Being Direct and communicative for the benefit of all parties</li>
      <li>Working for the Benefit of the company, client and team members</li>
      <li>Wanting to improve to create a better impact</li>
      <li>Having healthy rivalry</li>
    </ul>

    <h2 class="value-title title-curve">Be a Head of Curve:</h2>
    <ul class="value-list list-curve">
      <li>Having the confidence to break through barriers which arise</li>
      <li>Desire to grow and learn towards establishment and agreed goal</li>
      <li>Getting off the sidelines and get into the game</li>
      <li>Keeping the end game in mind having due regard to processes and milestones</li>
      <li>Self starter and works on own initiative</li>
      <li>Diligent and impactful in your field of responsibility</li>
    </ul>

    <h2 class="value-title title-truth">Truth and Honesty</h2>
    <ul class="value-list list-truth">
      <li>Having the confidence to break through barriers which arise</li>
      <li>Have the confidence and ability to speak what you really want to communicate</li>
      <li>Being truthful to yourself, clients and colleagues to find the innovations that lie within</li>
      <li>Seeking the truth by opening things up for discussion</li>
      <li>Being Optimistic</li>
    </ul>
  </section>

  <div class="photo photo-sand" role="img" aria-label="Photo of the words Good Vibes Only written in sand"></div>
  <div class="photo photo-growth" role="img" aria-label="Photo of a businessman stepping up sketched bar-chart steps in front of a board of drawn diagrams"></div>
  <div class="photo photo-stones" role="img" aria-label="Photo of engraved stones reading Truth, Courage and Hope among pine branches and cones"></div>
</body>
</html>
```